Business / Discount Card

Looking to create a 2 sided business card. Front side to say "Thanks for flying with Skyward Drifts" then have link to "In-Flight Photos, www.skywarddrifts-example.com.au, password: skyward" Back side of card to have company logo, phone number, facebook & instagram logo and #skywarddrifts. Also included on this side will be discount text "Book again and save 10%. Use discount code: skyward10"Round Corner Card Templates are attached. Please ensure dimensions are correct.Thanks,

Font styles to use
Sans Serif

Colors
33a6d7
ffffff
000000

Requirements
Must have
• Logo
• Blue, White and Black color scheme

```html
<!DOCTYPE html>
<html lang="en">
<head>
<meta charset="utf-8">
<title>Skyward Drifts – Business / Discount Card</title>
<link rel="stylesheet" href="https://fonts.googleapis.com/css2?family=Nunito+Sans:wght@400;700;800&display=swap">
<style>
  :root {
    --sky-blue: #33a6d7;
    --ink-black: #0b0b0c;
    --paper-white: #ffffff;
    --soft-white: #f1f1f2;
    --backdrop: #3a3a3c;
    --card-radius: 30px;
  }
  * { box-sizing: border-box; margin: 0; padding: 0; }
  html, body {
    width: 1200px; height: 1021px; overflow: hidden;
    background: var(--backdrop);
    font-family: "Nunito Sans", Arial, sans-serif;
  }
  .sheet {
    width: 1200px; height: 1021px;
    display: flex; flex-direction: column; align-items: center; justify-content: center;
    gap: 44px;
  }
  .card {
    position: relative;
    width: 740px; height: 450px;
    border-radius: var(--card-radius);
    background: var(--ink-black);
    overflow: hidden;
    box-shadow: 0 12px 30px rgba(0,0,0,.45);
  }

  /* Thank-you side */
  .thanks-side .message {
    position: absolute; left: 70px; top: 110px; width: 380px;
    text-align: right;
  }
  .thanks-side .headline {
    color: var(--sky-blue);
    font-weight: 800; font-size: 31px; line-height: 1.2;
  }
  .thanks-side .photos {
    margin-top: 40px;
    color: var(--paper-white);
    font-size: 19px; line-height: 1.3;
    text-align: center; padding-left: 80px;
  }
  .thanks-side .photos .site { font-weight: 700; font-size: 18px; }
  .thanks-side .photos .site b { color: var(--sky-blue); }
  .brand-mark {
    position: absolute; right: 60px; top: 120px; width: 220px;
    display: flex; flex-direction: column; align-items: center; gap: 20px;
  }
  .brand-mark .dot {
    width: 150px; height: 150px; border-radius: 50%;
    background: var(--sky-blue);
  }
  .brand-mark .name {
    color: var(--paper-white); font-weight: 800; font-size: 28px;
  }

  /* Logo & discount side */
  .logo-lockup {
    position: absolute; left: 0; right: 0; top: 70px;
    display: flex; align-items: center; justify-content: center; gap: 22px;
  }
  .logo-lockup .dot {
    width: 78px; height: 78px; border-radius: 50%; background: var(--paper-white);
  }
  .logo-lockup .name {
    color: var(--sky-blue); font-weight: 800; font-size: 70px; letter-spacing: 1px;
  }
  .contact-band {
    position: absolute; left: 0; right: 0; top: 268px; height: 92px;
    background: var(--sky-blue);
    display: flex; align-items: center;
    color: var(--paper-white); font-size: 22px;
  }
  .contact-item {
    position: relative; flex: 1; text-align: center; padding-top: 8px;
  }
  .contact-item + .contact-item::before {
    content: ""; position: absolute; left: 0; top: 6px; bottom: -4px;
    border-left: 2px solid var(--paper-white);
  }
  .contact-icon {
    position: absolute; left: 50%; top: -44px; transform: translateX(-50%);
    width: 36px; height: 36px; border-radius: 50%;
    background: var(--sky-blue); border: 2px solid var(--paper-white);
    display: flex; align-items: center; justify-content: center;
  }
  .discount-band {
    position: absolute; left: 0; right: 0; top: 360px; bottom: 0;
    background: var(--soft-white);
    display: flex; align-items: center; justify-content: center;
    color: var(--ink-black); font-size: 24px;
  }
  .discount-band strong { color: var(--sky-blue); font-weight: 800; }
</style>
</head>
<body>
<main class="sheet">

  <section class="card thanks-side" aria-label="Thank-you side">
    <div class="message">
      <p class="headline">Thanks for flying<br>with Skyward Drifts</p>
      <p class="photos">
        In-Flight Photos<br>
        <span class="site">www.<b>skywarddrifts-example</b>.com.au</span><br>
        password: skyward
      </p>
    </div>
    <div class="brand-mark">
      <span class="dot"></span>
      <span class="name">Skyward Drifts</span>
    </div>
  </section>

  <section class="card logo-side" aria-label="Logo and discount side">
    <div class="logo-lockup">
      <span class="dot"></span>
      <span class="name">Skyward Drifts</span>
    </div>

    <div class="contact-band">
      <div class="contact-item">
        <span class="contact-icon">
          <svg width="18" height="18" viewBox="0 0 24 24" aria-hidden="true">
            <path fill="#fff" d="M6.6 10.8a15 15 0 0 0 6.6 6.6l2.2-2.2c.3-.3.7-.4 1-.2 1.1.4 2.3.6 3.6.6.6 0 1 .4 1 1V20c0 .6-.4 1-1 1A17 17 0 0 1 3 4c0-.6.4-1 1-1h3.5c.6 0 1 .4 1 1 0 1.3.2 2.5.6 3.6.1.3 0 .7-.2 1z"/>
          </svg>
        </span>
        (123) 456-7890
      </div>
      <div class="contact-item">
        <span class="contact-icon" aria-hidden="true"></span>
        #skywarddrifts
      </div>
      <div class="contact-item">
        <span class="contact-icon" aria-hidden="true"></span>
        /skywarddrifts
      </div>
    </div>

    <div class="discount-band">
      <p>Book again and <strong>SAVE 10%</strong> - Use discount code: <strong>skyward10</strong></p>
    </div>
  </section>

</main>
</body>
</html>
```